Need a business card for our overland brand!

We had the logo made and we need a great design for our business card. Use the logo provide or tweak it however you see fit.

Contact Information for Business Card

Name, Title, Telephone, email, website

```html
<!DOCTYPE html>
<html lang="en">
<head>
<meta charset="utf-8">
<title>Ridgeway Trails – Business Card</title>
<link href="https://fonts.googleapis.com/css2?family=Lato:wght@400;700;900&display=swap" rel="stylesheet">
<style>
  :root {
    --page-bg: #e9ecef;
    --card-white: #ffffff;
    --blue-deep: #0a5fa8;
    --blue: #1f7fcf;
    --blue-light: #3aa6e0;
    --navy: #1d2a3a;
    --ink: #1f2328;
  }
  * { box-sizing: border-box; margin: 0; padding: 0; }
  html, body {
    width: 1200px; height: 900px; overflow: hidden;
    background: var(--page-bg);
    font-family: "Lato", sans-serif;
  }
  .sheet {
    width: 1200px; height: 900px;
    display: flex; flex-direction: column;
    align-items: center; justify-content: center; gap: 60px;
  }
  .card {
    position: relative;
    width: 600px; height: 343px;
    border-radius: 18px;
    overflow: hidden;
    background: var(--card-white);
    box-shadow: 0 8px 24px rgba(0,0,0,0.18);
  }
  .card-sides { position: absolute; inset: 0; width: 100%; height: 100%; display: block; }
  .stop-deep { stop-color: var(--blue-deep); }
  .stop-mid { stop-color: var(--blue); }
  .stop-light { stop-color: var(--blue-light); }

  .brand-name {
    position: absolute;
    font-weight: 900;
    color: var(--navy);
    text-transform: uppercase;
    line-height: 0.95;
    letter-spacing: 0.5px;
  }
  .card-front .brand-name { left: 0; right: 0; top: 110px; text-align: center; font-size: 44px; }
  .card-back .brand-name { left: 168px; top: 38px; font-size: 22px; }

  .contact-line {
    display: flex; align-items: center; gap: 10px;
    font-size: 15px; color: var(--ink);
  }
  .contact-icon { width: 18px; height: 18px; flex: none; }
  .card-front .web-line { position: absolute; left: 0; right: 0; top: 236px; justify-content: center; font-size: 17px; }

  .person { position: absolute; left: 196px; top: 140px; }
  .person-name { font-size: 30px; font-weight: 400; color: var(--blue-light); text-transform: uppercase; letter-spacing: 1px; }
  .person-title { font-size: 16px; color: var(--ink); margin-top: 2px; }
  .contact-list { position: absolute; left: 210px; top: 230px; display: flex; flex-direction: column; gap: 8px; }
</style>
</head>
<body>
<main class="sheet">

  <section class="card card-front" aria-label="Business card front">
    <svg class="card-sides" viewBox="0 0 350 200" preserveAspectRatio="none" role="img" aria-label="Blue faceted geometric pattern on both sides">
      <defs>
        <linearGradient id="front-side-left" x1="0" y1="0" x2="1" y2="1">
          <stop offset="0" class="stop-mid"/>
          <stop offset="0.5" class="stop-deep"/>
          <stop offset="1" class="stop-light"/>
        </linearGradient>
        <linearGradient id="front-side-right" x1="1" y1="0" x2="0" y2="1">
          <stop offset="0" class="stop-deep"/>
          <stop offset="0.5" class="stop-mid"/>
          <stop offset="1" class="stop-light"/>
        </linearGradient>
      </defs>
      <polygon fill="url(#front-side-left)" points="0,0 84,0 63,104 105,200 0,200"/>
      <polygon fill="url(#front-side-right)" points="238,0 350,0 350,200 266,200 294,96"/>
    </svg>
    <div class="brand-name">Ridgeway<br>Trails</div>
    <div class="contact-line web-line">
      <svg class="contact-icon" viewBox="0 0 20 20" aria-hidden="true"><circle cx="10" cy="10" r="10" fill="#3aa6e0"/><circle cx="10" cy="10" r="5" fill="none" stroke="#fff" stroke-width="1.3"/><path d="M5 10h10M10 5c-2 3-2 7 0 10M10 5c2 3 2 7 0 10" fill="none" stroke="#fff" stroke-width="1"/></svg>
      <span>www.marcushale.com</span>
    </div>
  </section>

  <section class="card card-back" aria-label="Business card back">
    <svg class="card-sides" viewBox="0 0 350 200" preserveAspectRatio="none" role="img" aria-label="Blue faceted geometric pattern on both sides">
      <defs>
        <linearGradient id="back-side-left" x1="0" y1="0" x2="1" y2="1">
          <stop offset="0" class="stop-mid"/>
          <stop offset="0.5" class="stop-deep"/>
          <stop offset="1" class="stop-light"/>
        </linearGradient>
        <linearGradient id="back-side-right" x1="1" y1="0" x2="0" y2="1">
          <stop offset="0" class="stop-deep"/>
          <stop offset="0.5" class="stop-mid"/>
          <stop offset="1" class="stop-light"/>
        </linearGradient>
      </defs>
      <polygon fill="url(#back-side-left)" points="0,0 84,0 63,104 105,200 0,200"/>
      <polygon fill="url(#back-side-right)" points="238,0 350,0 350,200 266,200 294,96"/>
    </svg>
    <div class="brand-name">Ridgeway<br>Trails</div>
    <div class="person">
      <div class="person-name">Marcus Hale</div>
      <div class="person-title">Director</div>
    </div>
    <div class="contact-list">
      <div class="contact-line">
        <svg class="contact-icon" viewBox="0 0 20 20" aria-hidden="true"><circle cx="10" cy="10" r="10" fill="#3aa6e0"/><path d="M7 5.5l1.8 0 .8 2.3-1.2.9a6 6 0 0 0 2.9 2.9l.9-1.2 2.3.8v1.8c0 .6-.5 1-1 1A8 8 0 0 1 6 6.5c0-.5.4-1 1-1z" fill="#fff"/></svg>
        <span>+880-145-2290-317</span>
      </div>
      <div class="contact-line">
        <svg class="contact-icon" viewBox="0 0 20 20" aria-hidden="true"><circle cx="10" cy="10" r="10" fill="#3aa6e0"/><rect x="5" y="6.5" width="10" height="7" rx="1" fill="#fff"/><path d="M5.5 7l4.5 3.5L14.5 7" fill="none" stroke="#3aa6e0" stroke-width="1"/></svg>
        <span>marcushale@mail.com</span>
      </div>
      <div class="contact-line">
        <svg class="contact-icon" viewBox="0 0 20 20" aria-hidden="true"><circle cx="10" cy="10" r="10" fill="#3aa6e0"/><circle cx="10" cy="10" r="5" fill="none" stroke="#fff" stroke-width="1.3"/><path d="M5 10h10M10 5c-2 3-2 7 0 10M10 5c2 3 2 7 0 10" fill="none" stroke="#fff" stroke-width="1"/></svg>
        <span>www.marcushale.com</span>
      </div>
    </div>
  </section>

</main>
</body>
</html>
```